bryn calvo website design

An IT support and IT Security Company - just use dummy text for now for the design. Examples of sites we like the looks and feel of but need it more professional feel are like: www.quorvatech.uk.com , www.halvion.co.uk, www.truvexa.com/professional/, www.zul.com, www.mivlen.com,

Best to message me if you have any questions

Target Market(s)

small to medium UK based companies that require IT support services

Industry/Entity Type

It Company

Contact Information for Business Card

use dummy name, telephone and email for now, will provide details later.

Logo Text

bryn calvo (and then below the logo it should say "your IT, networks and security partner")

Coding

Coded - Design and coding required

Number of Pages Required

5+ page

Colors

Designer to choose colors to be used in the design.

Requirements
Must have
• must be professional, yet simple and clear that this is a serious IT support and IT security company.
Nice to have
• 1)The website homepage must have professional quality pictures of IT support or London city skyline or any picture that projects friendly business partners, professionalism and ready to serve.
• 2) Home page needs to include tabs for following pages 'Services' , 'About Us' , 'Contact Us' 'Home'
• 3) Website built customised using wordpress is ideal and easy for us to manage.
• more room for boxed options from homepage (with pic or image in background)
Should not have
• no checkout trolleys or payment options.

```html
<!DOCTYPE html>
<html lang="en">
<head>
<meta charset="utf-8">
<title>Bryn Calvo – IT Support and IT Security</title>
<link href="https://fonts.googleapis.com/css2?family=Raleway:wght@400;500;600;700;800&display=swap" rel="stylesheet">
<style>
:root{
  --brand:#0cb4e8;
  --brand-dark:#0699c9;
  --ink:#111;
  --text:#666;
  --white:#fff;
  --footer:#050505;
  --footer-line:#3a3a3a;
  --field:#3b3b3b;
}
*{margin:0;padding:0;box-sizing:border-box}
html,body{width:1200px;height:2961px;overflow:hidden}
body{position:relative;background:var(--white);font-family:"Raleway",sans-serif;color:var(--ink)}
.abs{position:absolute}
a{color:inherit;text-decoration:none}

/* header */
.site-header{left:0;top:0;width:1200px;height:89px;background:var(--white)}
.brand{left:78px;top:18px;font-size:44px;font-weight:600;color:var(--brand);letter-spacing:-.5px}
.nav-link{top:37px;font-size:16px;font-weight:500;text-transform:uppercase;white-space:nowrap;line-height:20px}
.nav-link.home{left:612px;color:var(--brand);display:flex;align-items:center;gap:10px}
.nav-link.about{left:718px}
.nav-link.services{left:847px}
.nav-link.contact{left:961px}
.search-icon{left:1105px;top:38px}

/* hero */
.hero{left:0;top:89px;width:1200px;height:588px;
  background:linear-gradient(180deg,#3d6d8e 0%,#5d8aa6 35%,#3f5864 62%,#6b5a3a 82%,#2e3a3e 100%)}
.hero-title{left:0;top:225px;width:1200px;text-align:center;color:var(--white);font-size:50px;font-weight:700;line-height:63px}
.hero-copy{left:220px;top:356px;width:760px;text-align:center;color:var(--white);font-size:18px;font-weight:700;line-height:29px}
.hero-arrow{left:30px;top:375px}
.btn{display:flex;align-items:center;justify-content:center;background:var(--brand);color:var(--white);font-weight:700;font-size:20px;text-transform:uppercase}
.hero-btn{left:507px;top:430px;width:186px;height:56px}

/* service cards */
.service-card{top:657px;width:375px;height:291px;background:var(--brand);color:var(--white);text-align:center;box-shadow:0 26px 28px -18px rgba(0,0,0,.35)}
.service-card.support{left:201px}
.service-card.security{left:624px}
.service-badge{left:104px;top:-83px;width:166px;height:166px;border-radius:50%;background:var(--white);border:4px solid var(--brand);display:flex;align-items:center;justify-content:center}
.service-icon{width:96px;height:96px;border-radius:50%;background:#222}
.service-title{position:absolute;left:0;top:101px;width:100%;font-size:28px;font-weight:700}
.service-text{position:absolute;left:40px;top:152px;width:295px;font-size:13.5px;font-weight:600;line-height:27px}
.service-more{position:absolute;left:170px;top:245px}

/* welcome */
.section-title{left:0;width:1200px;text-align:center;font-size:44px;font-weight:700;color:var(--ink)}
.welcome-title{top:1012px}
.welcome-copy{left:180px;width:840px;text-align:center;font-size:14px;line-height:27px;color:var(--text)}
.welcome-copy.one{top:1082px}
.welcome-copy.two{top:1151px}
.welcome-btn{left:507px;top:1246px;width:186px;height:57px}

/* about */
.about{left:0;top:1366px;width:1200px;height:573px;background:linear-gradient(110deg,#23b2e2 0%,#5ccbef 45%,#1aa6d8 75%,#58c6ea 100%)}
.about-title{left:79px;top:1455px;font-size:40px;font-weight:700;color:var(--ink)}
.about-copy{left:79px;width:625px;font-size:14px;font-weight:600;line-height:27.5px;color:var(--white)}
.about-copy.one{top:1522px}
.about-copy.two{top:1648px}
.about-btn{left:79px;top:1771px;width:184px;height:55px;background:var(--brand-dark)}
.about-photo{left:760px;top:1392px;width:340px;height:547px;border-radius:170px 170px 0 0;background:linear-gradient(180deg,#d9b49a 0%,#c99c7d 25%,#8f8f8f 45%,#777 100%)}

/* partners */
.partners{left:78px;top:1984px;width:1044px;height:72px;display:flex;justify-content:space-between;align-items:center}
.partner{height:46px;background:#3a3a3a;opacity:.85}
.partner.a{width:186px;border-radius:2px}
.partner.b{width:106px;border-radius:2px;background:#8a8a8a}
.partner.c{width:208px;border-radius:2px}
.partner.d{width:150px;border-radius:23px;background:#8a8a8a}
.partner.e{width:46px;border-radius:50%}
.partners-shadow{left:210px;top:2080px;width:780px;height:18px;border-radius:50%;box-shadow:0 10px 12px -6px rgba(0,0,0,.35)}

/* news */
.news-title{top:2144px}
.news-card{top:2213px;width:333px;height:340px}
.news-card.n1{left:77px}
.news-card.n2{left:434px}
.news-card.n3{left:790px}
.news-image{position:absolute;left:0;top:0;width:333px;height:199px}
.news-card.n1 .news-image{background:linear-gradient(135deg,#1f3f66,#3fb0d8 60%,#1b3550)}
.news-card.n2 .news-image{background:linear-gradient(135deg,#e7e7e5,#b9b7b2 55%,#8a8782)}
.news-card.n3 .news-image{background:linear-gradient(135deg,#1f2d44,#354766 50%,#101824)}
.news-date{position:absolute;left:0;top:166px;width:71px;height:89px;background:var(--brand);color:var(--white);text-align:center;padding-top:8px}
.news-day{font-size:34px;font-weight:600;line-height:40px}
.news-month{font-size:18px;font-weight:700;line-height:28px}
.news-head{position:absolute;left:87px;top:211px;width:250px;font-size:17px;font-weight:700;line-height:26px}
.news-text{position:absolute;left:0;top:274px;width:333px;font-size:13.5px;line-height:26px;color:var(--text)}

/* footer */
.site-footer{left:0;top:2612px;width:1200px;height:290px;background:var(--footer)}
.footer-head{top:2644px;font-size:15px;font-weight:700;color:var(--brand);text-transform:uppercase}
.sitemap{left:79px;top:2678px;width:228px;list-style:none}
.sitemap li{height:44px;border-bottom:1px solid var(--footer-line);color:var(--white);font-size:13px;display:flex;align-items:center;gap:14px}
.sitemap li:last-child{border-bottom:none}
.sitemap li::before{content:"";width:6px;height:6px;border-radius:50%;background:var(--brand)}
.field{left:345px;width:226px;height:33px;background:var(--field);color:#ccc;font-size:11px;padding:9px 7px}
.field.msg{height:66px}
.send{left:345px;top:2829px;width:226px;height:32px;font-size:15px;font-weight:500}
.touch-row{left:612px;width:245px;color:var(--white);font-size:13px;line-height:20px}
.touch-name{color:var(--brand);font-size:17px;font-weight:600}
.touch-divider{left:612px;width:245px;height:1px;background:var(--footer-line)}
.footer-brand{left:878px;top:2705px;font-size:44px;font-weight:600;color:var(--brand)}
.social{top:2773px;width:42px;height:42px;border-radius:50%;border:2px solid var(--white)}
.social.s1{left:926px;background:var(--brand);border-color:var(--brand)}
.social.s2{left:978px}
.social.s3{left:1030px}
.copyright{left:0;top:2902px;width:1200px;height:59px;background:var(--brand);color:var(--white);font-size:13px;font-weight:600;display:flex;align-items:center;justify-content:center}
</style>
</head>
<body>

<header class="site-header abs">
  <div class="brand abs">Bryn Calvo</div>
  <nav>
    <a class="nav-link home abs" href="#">Home
      <svg width="14" height="9" viewBox="0 0 14 9"><path d="M0 0h14L7 9z" fill="#0cb4e8"/></svg></a>
    <a class="nav-link about abs" href="#">About Us</a>
    <a class="nav-link services abs" href="#">Services</a>
    <a class="nav-link contact abs" href="#">Contact Us</a>
  </nav>
  <svg class="search-icon abs" width="18" height="18" viewBox="0 0 18 18"><circle cx="7.5" cy="7.5" r="5.5" fill="none" stroke="#111" stroke-width="2.6"/><path d="M11.5 11.5l5 5" stroke="#111" stroke-width="3" stroke-linecap="round"/></svg>
</header>

<section class="hero abs" role="img" aria-label="London riverside skyline at dusk with clock tower, parliament and bridge"></section>
<svg class="hero-arrow abs" width="20" height="60" viewBox="0 0 20 60"><path d="M18 2L3 30l15 28" fill="none" stroke="#fff" stroke-width="2" opacity=".8"/></svg>
<h1 class="hero-title abs">IT SUPPORT AND IT SECURITY<br>COMPANY</h1>
<p class="hero-copy abs">Lorem Ipsum is simply dummy text of the printing and typesetting psum has been the industry's standard Lorem Ipsum is simply dummy text of the printing.</p>
<a class="btn hero-btn abs" href="#">Contact Us</a>

<article class="service-card support abs">
  <div class="service-badge abs"><div class="service-icon" role="img" aria-label="Support agent with headset icon"></div></div>
  <h3 class="service-title">It Support</h3>
  <p class="service-text">Lorem Ipsum is simply dummy text of the printing and typesetting industry. Lorem Ipsum has been the industry's standard</p>
  <svg class="service-more" width="34" height="14" viewBox="0 0 34 14"><path d="M0 7h30M24 1l7 6-7 6" fill="none" stroke="#fff" stroke-width="3"/></svg>
</article>
<article class="service-card security abs">
  <div class="service-badge abs"><div class="service-icon" role="img" aria-label="Globe with security shield icon"></div></div>
  <h3 class="service-title">It Security</h3>
  <p class="service-text">Lorem Ipsum is simply dummy text of the printing and typesetting industry. Lorem Ipsum has been the industry's standard</p>
  <svg class="service-more" width="34" height="14" viewBox="0 0 34 14"><path d="M0 7h30M24 1l7 6-7 6" fill="none" stroke="#fff" stroke-width="3"/></svg>
</article>

<h2 class="section-title welcome-title abs">Welcome To Bryn Calvo</h2>
<p class="welcome-copy one abs">Lorem Ipsum is simply dummy text of the printing and typesetting industry. Lorem Ipsum has been the industry's standard dummy text ever since the when an unknown printer took a galley of type and sBryn Calvocrambled.</p>
<p class="welcome-copy two abs">Lorem Ipsum is simply dummy text of the printing and typesetting industry. Lorem Ipsum has been the industry's standard dummy text ever since the when an unknown printer took a galley of type and sBryn Calvocrambled it to make a type specimen book. It has survived not only five centuries, but also the leap into electronic.</p>
<a class="btn welcome-btn abs" href="#">Learn More</a>

<section class="about abs" role="img" aria-label="Blue toned background of hands working on a laptop with network graphics"></section>
<h2 class="about-title abs">About Us</h2>
<p class="about-copy one abs">Lorem Ipsum is simply dummy text of the printing and typesetting industry. Lorem Ipsum has been the industry's standard dummy text ever since the when an unknown printer took a galley of type and sBryn Calvocrambled it to make a type specimen book. It has survived not only five centuries, but also the leap into electronic.</p>
<p class="about-copy two abs">Lorem Ipsum is simply dummy text of the printing and typesetting industry. Lorem Ipsum has been the industry's standard dummy text ever since the when an unknown printer took a galley of type and sBryn Calvocrambled it to make a type specimen book. It has survived not only five centuries, but also the leap into electronic.</p>
<a class="btn about-btn abs" href="#">Learn More</a>
<div class="about-photo abs" role="img" aria-label="Smiling businessman in grey shirt with arms crossed"></div>

<div class="partners abs">
  <div class="partner a"></div><div class="partner b"></div><div class="partner c"></div><div class="partner d"></div><div class="partner e"></div>
</div>
<div class="partners-shadow abs"></div>

<h2 class="section-title news-title abs">Latest News</h2>
<article class="news-card n1 abs">
  <div class="news-image" role="img" aria-label="Person typing on laptop with glowing security icons"></div>
  <div class="news-date"><div class="news-day">07</div><div class="news-month">FEB</div></div>
  <h4 class="news-head">Lorem Ipsum is the simply text of the printing &amp; type.</h4>
  <p class="news-text">Lorem Ipsum is the simply dummy text of the printing and typesetting industry. Lorem Ipsum has the been the print text of print industry.</p>
</article>
<article class="news-card n2 abs">
  <div class="news-image" role="img" aria-label="Bright open-plan office with people at desks"></div>
  <div class="news-date"><div class="news-day">08</div><div class="news-month">FEB</div></div>
  <h4 class="news-head">Lorem Ipsum is the simply text of the printing &amp; type.</h4>
  <p class="news-text">Lorem Ipsum is the simply dummy text of the printing and typesetting industry. Lorem Ipsum has the been the print text of print industry.</p>
</article>
<article class="news-card n3 abs">
  <div class="news-image" role="img" aria-label="Technician with laptop in a server room"></div>
  <div class="news-date"><div class="news-day">09</div><div class="news-month">FEB</div></div>
  <h4 class="news-head">Lorem Ipsum is the simply text of the printing &amp; type.</h4>
  <p class="news-text">Lorem Ipsum is the simply dummy text of the printing and typesetting industry. Lorem Ipsum has the been the print text of print industry.</p>
</article>

<footer class="site-footer abs"></footer>
<div class="footer-head abs" style="left:79px">Sitemap</div>
<ul class="sitemap abs">
  <li>Home</li><li>About Us</li><li>Services</li><li>Contact Us</li>
</ul>

<div class="footer-head abs" style="left:345px">Contact Us</div>
<div class="field abs" style="top:2690px">Name</div>
<div class="field abs" style="top:2725px">E-Mail</div>
<div class="field msg abs" style="top:2760px">Message</div>
<div class="btn send abs">SEND</div>

<div class="footer-head abs" style="left:612px">Keep In Touch</div>
<svg class="abs" style="left:612px;top:2686px" width="18" height="22" viewBox="0 0 18 22"><path d="M8 0h2v22H8zM1 3h14l3 3-3 3H1zM17 11H3l-3 3 3 3h14z" fill="#0cb4e8"/></svg>
<div class="touch-row abs" style="top:2684px;left:646px;width:210px"><div class="touch-name">Bryn Calvo</div>101 - Lorem ipsum is simple text of print and type setting.</div>
<div class="touch-divider abs" style="top:2765px"></div>
<svg class="abs" style="left:612px;top:2777px" width="20" height="20" viewBox="0 0 24 24"><path d="M6.6 10.8a15 15 0 006.6 6.6l2.2-2.2c.3-.3.7-.4 1-.2 1.1.4 2.3.6 3.6.6.6 0 1 .4 1 1V20c0 .6-.4 1-1 1A17 17 0 013 4c0-.6.4-1 1-1h3.5c.6 0 1 .4 1 1 0 1.3.2 2.5.6 3.6.1.3 0 .7-.2 1z" fill="#0cb4e8"/></svg>
<div class="touch-row abs" style="top:2777px;left:646px">123 456 7890</div>
<div class="touch-divider abs" style="top:2808px"></div>
<svg class="abs" style="left:612px;top:2822px" width="20" height="15" viewBox="0 0 20 15"><rect width="20" height="15" fill="#0cb4e8"/><path d="M0 0l10 8 10-8" fill="none" stroke="#050505" stroke-width="1.6"/></svg>
<div class="touch-row abs" style="top:2820px;left:646px">info@bryncalvo.com</div>

<div class="footer-brand abs">Bryn Calvo</div>
<div class="social s1 abs"></div>
<div class="social s2 abs"></div>
<div class="social s3 abs"></div>

<div class="copyright abs">©Bryn Calvo - 2018 All Right Reserved.</div>

</body>
</html>
```